Progressive/contemporary business card design for successful Startups as a Service Company

New logo launched in 2020. New website launched in 2021. Now that COVID is (mostly) behind us, I'm networking with more people and need a business card that matches the company/logo design aesthetic.

```html
<!DOCTYPE html>
<html lang="en">
<head>
<meta charset="utf-8">
<title>Keystone Launch – Business Card</title>
<link rel="stylesheet" href="https://fonts.googleapis.com/css2?family=Montserrat:wght@400;500&family=Open+Sans:ital,wght@0,400;0,700;1,400&display=swap">
<style>
  :root {
    --backdrop: #2a2a2a;
    --card: #1c1c1c;
    --logo-ink: #e6e6e6;
    --text: #f2f2f2;
    --muted: #9a9a9a;
    --blue: #1fa3e0;
    --magenta: #d4178f;
    --purple: #8a2ea6;
    --green: #5cb83a;
    --orange: #f58a1f;
    --yellow: #f7c21b;
  }
  * { box-sizing: border-box; margin: 0; padding: 0; }
  html, body {
    width: 1200px; height: 900px; overflow: hidden;
    background: var(--backdrop);
  }
  .stage {
    width: 1200px; height: 900px;
    display: flex; flex-direction: column;
    align-items: center; justify-content: center; gap: 40px;
  }
  .card {
    position: relative;
    width: 665px; height: 380px;
    background: var(--card);
    box-shadow: 0 14px 30px rgba(0,0,0,.45);
    overflow: hidden;
  }
  .card__stripe {
    position: absolute; left: 0; right: 0; bottom: 0; height: 12px;
    background: linear-gradient(90deg,
      var(--blue) 0%, #2b7fd6 22%,
      var(--magenta) 30%, var(--purple) 45%,
      var(--green) 52%, #7fcf3a 72%,
      var(--orange) 80%, var(--yellow) 90%, var(--orange) 100%);
  }
  .brand-name {
    font-family: "Montserrat", sans-serif;
    font-weight: 400;
    color: var(--logo-ink);
    text-transform: uppercase;
    white-space: nowrap;
  }

  /* Front side */
  .card--front .brand-name {
    position: absolute; left: 48px; top: 158px;
    font-size: 27px; letter-spacing: 7px;
    width: 300px; line-height: 1.35;
  }
  .card__divider {
    position: absolute; left: 360px; top: 100px;
    width: 1px; height: 170px; background: var(--blue);
  }
  .contact {
    position: absolute; left: 380px; top: 100px;
    font-family: "Open Sans", sans-serif; color: var(--text);
    font-size: 15px; line-height: 1.45;
  }
  .contact__name {
    font-weight: 700; color: var(--blue);
    font-size: 21px; text-transform: uppercase; letter-spacing: .5px;
  }
  .contact__role { font-style: italic; color: var(--muted); margin-bottom: 6px; }
  .contact__address { margin-bottom: 6px; }
  .contact__line { display: flex; align-items: center; gap: 7px; }
  .contact__line svg { width: 13px; height: 13px; flex: none; }

  /* Back side */
  .card--back .brand-name {
    position: absolute; left: 0; right: 0; top: 160px;
    text-align: center; font-size: 36px; letter-spacing: 10px;
  }
</style>
</head>
<body>
<main class="stage">

  <section class="card card--front" aria-label="Business card front">
    <div class="brand-name">Keystone<br>Launch</div>
    <div class="card__divider"></div>
    <div class="contact">
      <p class="contact__name">Marcus Feldane</p>
      <p class="contact__role">President</p>
      <p class="contact__address">418 N Harbor Ave., Suite B<br>Lakeview, IL 60614</p>
      <p class="contact__line">
        <svg viewBox="0 0 16 16" aria-hidden="true"><path fill="var(--magenta)" d="M3.5 1.5l2.5 0 1 3.5-1.6 1.2a8 8 0 0 0 4.4 4.4L11 9l3.5 1v2.5c0 1-1 2-2 2C6.5 14.5 1.5 9.5 1.5 3.5c0-1 1-2 2-2z"/></svg>
        (555) 214-0387
      </p>
      <p class="contact__line">
        <svg viewBox="0 0 16 16" aria-hidden="true"><rect x="1" y="3" width="14" height="10" fill="var(--green)"/><path d="M1 3l7 6 7-6" fill="none" stroke="var(--card)" stroke-width="1.4"/></svg>
        hello@keystonelaunch.com
      </p>
      <p class="contact__line">
        <svg viewBox="0 0 16 16" aria-hidden="true"><circle cx="8" cy="8" r="6.5" fill="none" stroke="var(--orange)" stroke-width="1.6"/><path d="M1.5 8h13M8 1.5c-3 3.5-3 9.5 0 13M8 1.5c3 3.5 3 9.5 0 13" fill="none" stroke="var(--orange)" stroke-width="1.2"/></svg>
        www.keystonelaunch.co
      </p>
    </div>
    <div class="card__stripe"></div>
  </section>

  <section class="card card--back" aria-label="Business card back">
    <div class="brand-name">Keystone Launch</div>
    <div class="card__stripe"></div>
  </section>

</main>
</body>
</html>
```